Fernbrook Dwellings Business Card Design Project

Please create a custom Business Card Design for Fernbrook Dwellings. The logo is attached to this brief.Please include space for
Name Surname
Title (Solutions Specialist)
Phone
Email
Website
Industry/Entity Type
Business
Contact Information for Business Card
Reverse should be printed horizontally and have the following components:
Small version of the logo. (lowest priority)
The words "Real Estate Solutions Company"
A bulleted list (Note: Line breaks are suggestions only):
* BUY, RENOVATE, SELL and RENT:
RESIDENTIAL PROPERTIES
* MAKE CASH OFFERS ON HOUSES IN
ANY CONDITION and IN ANY SITUATION
* SELL PROPERTIES TO INVESTORS
* SOLVE COMPLEX REAL ESTATE
PROBLEMS and TITLE ISSUES
* PRIVATE MONEY INVESTMENT SERVICES
* PAY CASH REWARDS FOR REFERRALS
Included somewhere on the reverse should also be the following:
Office: (425) 555-0183
www.FernbrookDwellings.example
space for civic trade registry logo
Look and feel
Each slider illustrates characteristics of the customer's brand and the style your logo design should communicate.

```html
<!DOCTYPE html>
<html lang="en">
<head>
<meta charset="utf-8">
<title>Fernbrook Dwellings – Business Card</title>
<link rel="stylesheet" href="https://fonts.googleapis.com/css2?family=Montserrat:wght@500;600;700&family=Source+Sans+3:wght@400;600;700&display=swap">
<style>
  :root {
    --bg: #ede6d2;
    --paper: #ffffff;
    --brand-blue: #1b6fc2;
    --brand-yellow: #fcd116;
    --brand-green: #5cb335;
    --ink: #1d1d1f;
    --ink-soft: #3a3a3a;
    --rule: #555555;
  }
  * { box-sizing: border-box; margin: 0; padding: 0; }
  html, body { width: 1200px; height: 1200px; overflow: hidden; background: var(--bg); }
  body { position: relative; font-family: "Source Sans 3", sans-serif; color: var(--ink); }

  .card {
    position: absolute; left: 150px; width: 900px; height: 514px;
    background: var(--paper); overflow: hidden;
    box-shadow: 0 10px 30px rgba(90, 75, 40, 0.18);
  }
  .card--back { top: 60px; }
  .card--front { top: 626px; }

  /* Back side */
  .services-title {
    position: absolute; left: 58px; top: 52px;
    font-family: "Montserrat", sans-serif; font-weight: 600; font-size: 33px;
    color: var(--brand-blue);
  }
  .services-label {
    position: absolute; left: 62px; top: 104px;
    font-weight: 700; font-size: 28px; color: var(--ink);
  }
  .services-list { position: absolute; left: 62px; top: 150px; list-style: none; }
  .services-list li {
    display: flex; align-items: center; gap: 12px;
    font-size: 24px; line-height: 37px; color: var(--ink);
  }
  .tick-box { width: 20px; height: 20px; flex: none; }

  .back-contact {
    position: absolute; left: 62px; bottom: 50px;
    display: flex; gap: 46px; font-size: 27px; color: var(--brand-blue);
  }
  .back-contact span { display: flex; align-items: center; gap: 10px; }
  .contact-badge { width: 30px; height: 26px; flex: none; }

  .brand-mark { display: flex; align-items: center; gap: 12px; }
  .brand-mark__dot { border-radius: 50%; background: var(--brand-yellow); flex: none; }
  .brand-mark__name {
    font-family: "Montserrat", sans-serif; font-weight: 500; color: var(--brand-blue);
    white-space: nowrap;
  }
  .card--back .brand-mark { position: absolute; right: 48px; top: 56px; }
  .card--back .brand-mark__dot { width: 34px; height: 34px; }
  .card--back .brand-mark__name { font-size: 20px; }

  .registry-slot {
    position: absolute; right: 58px; top: 250px; width: 92px; height: 92px;
    border-radius: 50%; background: #e9eef5;
  }

  /* Front side */
  .card--front .brand-mark { position: absolute; left: 56px; top: 112px; }
  .card--front .brand-mark__dot { width: 50px; height: 50px; }
  .card--front .brand-mark__name { font-size: 29px; }

  .divider {
    position: absolute; left: 470px; top: 138px; width: 200px; height: 1px;
    background: var(--rule); transform: rotate(-2deg);
  }
  .person { position: absolute; right: 50px; top: 62px; text-align: right; }
  .person__name {
    font-family: "Montserrat", sans-serif; font-weight: 700; font-size: 30px;
    color: var(--brand-blue);
  }
  .person__title { font-size: 19px; color: var(--ink); margin-top: 2px; }

  .front-contact { position: absolute; left: 56px; top: 322px; list-style: none; }
  .front-contact li {
    display: flex; align-items: center; gap: 16px;
    font-size: 22px; line-height: 33px; color: var(--ink-soft);
  }
  .front-contact svg { width: 18px; height: 18px; flex: none; }

  .front-band { position: absolute; left: 0; bottom: 0; width: 900px; height: 130px; }
</style>
</head>
<body>

<!-- Reverse -->
<section class="card card--back" aria-label="Business card reverse">
  <h1 class="services-title">Real Estate Solutions Company</h1>
  <h2 class="services-label">Our Services:</h2>

  <div class="brand-mark">
    <span class="brand-mark__dot"></span>
    <span class="brand-mark__name">Fernbrook Dwellings</span>
  </div>

  <div class="registry-slot" role="img" aria-label="Space for civic trade registry badge"></div>

  <ul class="services-list">
    <li><svg class="tick-box" viewBox="0 0 20 20"><rect x="1" y="3" width="16" height="16" fill="none" stroke="#1b6fc2" stroke-width="2"/><path d="M4 11 l4 4 l10 -13" fill="none" stroke="#1b6fc2" stroke-width="2.2"/></svg>Buy, Renovate, Sell and Rent Residential Properties</li>
    <li><svg class="tick-box" viewBox="0 0 20 20"><rect x="1" y="3" width="16" height="16" fill="none" stroke="#1b6fc2" stroke-width="2"/><path d="M4 11 l4 4 l10 -13" fill="none" stroke="#1b6fc2" stroke-width="2.2"/></svg>Make Cash Offers on Houses in any Condition and in any Situation</li>
    <li><svg class="tick-box" viewBox="0 0 20 20"><rect x="1" y="3" width="16" height="16" fill="none" stroke="#1b6fc2" stroke-width="2"/><path d="M4 11 l4 4 l10 -13" fill="none" stroke="#1b6fc2" stroke-width="2.2"/></svg>Sell Properties to Investors</li>
    <li><svg class="tick-box" viewBox="0 0 20 20"><rect x="1" y="3" width="16" height="16" fill="none" stroke="#1b6fc2" stroke-width="2"/><path d="M4 11 l4 4 l10 -13" fill="none" stroke="#1b6fc2" stroke-width="2.2"/></svg>Solve Complex Real Estate Problems and Title Issues</li>
    <li><svg class="tick-box" viewBox="0 0 20 20"><rect x="1" y="3" width="16" height="16" fill="none" stroke="#1b6fc2" stroke-width="2"/><path d="M4 11 l4 4 l10 -13" fill="none" stroke="#1b6fc2" stroke-width="2.2"/></svg>Private Money Investment Services</li>
    <li><svg class="tick-box" viewBox="0 0 20 20"><rect x="1" y="3" width="16" height="16" fill="none" stroke="#1b6fc2" stroke-width="2"/><path d="M4 11 l4 4 l10 -13" fill="none" stroke="#1b6fc2" stroke-width="2.2"/></svg>Pay Cash Rewards for Referrals</li>
  </ul>

  <div class="back-contact">
    <span>
      <svg class="contact-badge" viewBox="0 0 30 26"><rect width="30" height="26" rx="5" fill="#1b6fc2"/><path d="M7 10 q8 -6 16 0 v3 h-4 v-2 h-8 v2 h-4 z" fill="#fff"/><rect x="9" y="14" width="12" height="7" rx="1" fill="#fff"/></svg>
      (425) 555-0183
    </span>
    <span>
      <svg class="contact-badge" viewBox="0 0 30 26"><rect width="30" height="26" rx="5" fill="#1b6fc2"/><circle cx="15" cy="13" r="7.5" fill="none" stroke="#fff" stroke-width="1.6"/><ellipse cx="15" cy="13" rx="3.2" ry="7.5" fill="none" stroke="#fff" stroke-width="1.4"/><path d="M7.5 13 h15" stroke="#fff" stroke-width="1.4"/></svg>
      www.FernbrookDwellings.example
    </span>
  </div>
</section>

<!-- Front -->
<section class="card card--front" aria-label="Business card front">
  <div class="brand-mark">
    <span class="brand-mark__dot"></span>
    <span class="brand-mark__name">Fernbrook Dwellings</span>
  </div>

  <div class="divider"></div>

  <div class="person">
    <div class="person__name">Marcus Ellery</div>
    <div class="person__title">Solutions Specialist</div>
  </div>

  <ul class="front-contact">
    <li><svg viewBox="0 0 18 18"><rect x="4" y="1" width="10" height="16" rx="2" fill="#1b6fc2"/><rect x="6" y="3" width="6" height="7" fill="#fff"/></svg>+0 508.555.0147</li>
    <li><svg viewBox="0 0 18 18"><rect x="1" y="4" width="16" height="11" fill="#1b6fc2"/><path d="M1 4 l8 6 l8 -6" fill="none" stroke="#fff" stroke-width="1.4"/></svg>marcus@fernbrookdwellings.example</li>
    <li><svg viewBox="0 0 18 18"><circle cx="9" cy="9" r="8" fill="#1b6fc2"/><ellipse cx="9" cy="9" rx="3.5" ry="8" fill="none" stroke="#fff" stroke-width="1.2"/><path d="M1 9 h16 M2.5 5 h13 M2.5 13 h13" stroke="#fff" stroke-width="1.1"/></svg>www.fernbrookdwellings.example</li>
  </ul>

  <svg class="front-band" viewBox="0 0 900 130" preserveAspectRatio="none" aria-hidden="true">
    <path d="M600 62 C700 40 800 22 900 10 L900 42 C800 50 710 62 640 78 Z" fill="var(--brand-yellow)"/>
    <path d="M0 92 L540 92 C610 92 640 76 690 70 C760 62 830 58 900 56 L900 130 L0 130 Z" fill="var(--brand-blue)"/>
  </svg>
</section>

</body>
</html>
```